Business Card Design Project

Want a modern business card.
Concern is that our email address is long and thus poses a design challenge.
Items like the company name can be omitted from text as it will be available via the logo.

Example:
Gerald Tunstall
President / CEO
Cell 555.304.1182
Office 555.617.2093
geraldt@korvantsolutionsgroup.example
www.korvantsolutionsgroup.example

Target Market(s)

Technical and executive level members of Information Technology companies in the Healthcare industry.

Industry/Entity Type

Business

Colors

Designer to choose colors to be used in the design.

Requirements
Nice to have
• Raised logo, but I am open.

```html
<!DOCTYPE html>
<html lang="en">
<head>
<meta charset="utf-8">
<title>Korvant Solutions Group – Business Card</title>
<link rel="stylesheet" href="https://fonts.googleapis.com/css2?family=PT+Sans:wght@400;700&display=swap">
<style>
  :root {
    --page: #ffffff;
    --navy: #1b2d6b;
    --ink: #1f2f66;
    --white: #ffffff;
    --sky-light: #eaf1fa;
    --sky-mid: #9fc0e4;
    --sky-deep: #3d76bd;
    --card-edge: #c9d6e6;
  }
  * { margin: 0; padding: 0; box-sizing: border-box; }
  html, body {
    width: 1200px; height: 582px; overflow: hidden;
    background: var(--page);
    font-family: "PT Sans", "Myriad Pro", Arial, sans-serif;
  }
  .canvas { position: relative; width: 1200px; height: 582px; }
  .card {
    position: absolute; top: 0; width: 531px; height: 344px;
    overflow: hidden; border: 1px solid var(--card-edge);
  }
  .card--front { left: 15px; }
  .card--back { left: 579px; }
  .artwork { position: absolute; inset: 0; }
  .card--front .artwork {
    background: linear-gradient(135deg, var(--sky-light) 0%, var(--sky-mid) 55%, var(--sky-deep) 100%);
  }
  .card--back .artwork {
    background: linear-gradient(160deg, var(--sky-deep) 0%, var(--sky-mid) 35%, var(--sky-light) 70%, var(--sky-mid) 100%);
  }
  .logo-band {
    position: absolute; left: 0; right: 0; top: 118px; height: 104px;
    background: linear-gradient(90deg, rgba(255,255,255,0.92) 0%, rgba(255,255,255,0.8) 70%, rgba(255,255,255,0.35) 100%);
  }
  .logo {
    position: absolute; left: 40px; top: 150px;
    display: flex; align-items: center; gap: 14px;
  }
  .logo__mark { width: 30px; height: 30px; background: var(--navy); }
  .logo__name {
    color: var(--navy); font-weight: 700; font-size: 34px; line-height: 40px;
  }
  .identity {
    position: absolute; right: 18px; top: 268px;
    color: var(--white); text-align: right; font-size: 20px; line-height: 28px;
  }
  .contact {
    position: absolute; right: 19px; top: 214px;
    color: var(--ink); text-align: right; font-size: 19px; line-height: 27px;
    list-style: none;
  }
</style>
</head>
<body>
<main class="canvas">
  <section class="card card--front">
    <div class="artwork" role="img" aria-label="Globe illustration showing the Americas in soft blues"></div>
    <div class="logo-band"></div>
    <div class="logo">
      <span class="logo__mark"></span>
      <span class="logo__name">Korvant Solutions Group</span>
    </div>
    <div class="identity">
      <p class="identity__name">Gerald Tunstall</p>
      <p class="identity__title">President / CEO</p>
    </div>
  </section>
  <section class="card card--back">
    <div class="artwork" role="img" aria-label="Close-up globe illustration showing North America in soft blues"></div>
    <ul class="contact">
      <li>Cell 555.304.1182</li>
      <li>Office 555.617.2093</li>
      <li>geraldt@korvantsolutionsgroup.example</li>
      <li>www.korvantsolutionsgroup.example</li>
    </ul>
  </section>
</main>
</body>
</html>
```